New LGBT Nightclub Crowdfunding Poster

We need it to read well for social media posts. All colors should look similar to Seattle’s Sports Teams color schemes.

The top should have: The logo prominently with the fans in the background photo. and then still center and important, "Coming soon!" "You can be part of the first in line for the amazing things happening". (The call to action is the purchase of these amazing deals for the first weekend open / passes. That should be clear).

```html
<!DOCTYPE html>
<html lang="en">
<head>
<meta charset="utf-8">
<title>The Rebound – Coming Soon</title>
<link href="https://fonts.googleapis.com/css2?family=Russo+One&family=Orbitron:wght@800;900&family=Roboto+Condensed:wght@400;700&display=swap" rel="stylesheet">
<style>
  :root {
    --stage: #f6dc4f;
    --turf: #5b973a;
    --turf-deep: #4c8530;
    --navy: #1b2455;
    --white: #ffffff;
    --lights-warm: #d98a6a;
    --lights-cool: #6f7fa0;
  }
  * { box-sizing: border-box; margin: 0; padding: 0; }
  html, body { width: 1200px; height: 840px; overflow: hidden; }
  body { background: var(--stage); position: relative; font-family: "Roboto Condensed", sans-serif; }

  .poster {
    position: absolute; left: 317px; top: 20px; width: 566px; height: 800px;
    background: var(--turf); overflow: hidden;
    box-shadow: 0 6px 18px rgba(0,0,0,0.18);
  }
  .poster__crowd {
    position: absolute; left: 0; top: 0; width: 100%; height: 440px;
    background:
      radial-gradient(ellipse at 75% 18%, rgba(255,240,220,0.9), rgba(255,240,220,0) 45%),
      radial-gradient(ellipse at 15% 25%, rgba(255,230,190,0.7), rgba(255,230,190,0) 40%),
      linear-gradient(180deg, #4a4f5e 0%, var(--lights-cool) 22%, var(--lights-warm) 48%, #8a6f62 62%, var(--turf) 100%);
  }

  .brand {
    position: absolute; left: 165px; top: 50px; width: 236px; height: 236px;
    border-radius: 50%; background: var(--navy);
    display: flex; flex-direction: column; align-items: center; justify-content: center;
    color: var(--white); font-family: "Russo One", sans-serif; text-align: center;
  }
  .brand__name { font-size: 34px; line-height: 1.05; letter-spacing: 1px; }
  .brand__area { font-size: 17px; margin-top: 14px; letter-spacing: 2px; }

  .headline {
    position: absolute; left: 0; width: 100%; text-align: center;
    font-family: "Russo One", sans-serif; color: var(--white);
    line-height: 0.86; text-shadow: 4px 5px 0 rgba(40,60,30,0.45);
    transform: rotate(-4deg);
  }
  .headline--top { top: 262px; font-size: 124px; letter-spacing: -3px; }
  .headline--bottom { top: 372px; font-size: 118px; letter-spacing: -2px; left: 20px; }

  .tagline {
    position: absolute; left: 68px; top: 505px; width: 440px; text-align: center;
    font-family: "Orbitron", sans-serif; font-weight: 900; color: var(--navy);
    font-size: 27px; line-height: 1.1; text-transform: uppercase;
    transform: rotate(-5deg) skewX(-6deg);
  }

  .deals {
    position: absolute; left: 20px; top: 636px; width: 526px; height: 146px;
    border: 2px solid var(--navy); border-top: none;
  }
  .deals::before, .deals::after {
    content: ""; position: absolute; top: 0; height: 2px; width: 22px; background: var(--navy);
  }
  .deals::before { left: 0; }
  .deals::after { right: 0; }
  .deals__title {
    position: absolute; top: -7px; left: 28px; right: 28px; text-align: center;
    font-family: "Orbitron", sans-serif; font-weight: 800; color: var(--white);
    font-size: 11px; line-height: 1; letter-spacing: 0; white-space: nowrap;
  }
  .deals__columns {
    position: absolute; top: 18px; left: 14px; right: 14px; bottom: 8px;
    display: grid; grid-template-columns: 1fr 1fr; column-gap: 12px;
  }
  .deals__col + .deals__col { border-left: 1.5px solid var(--navy); padding-left: 8px; }
  .deal { color: var(--white); font-size: 8.4px; line-height: 1.22; margin-bottom: 8px; }
  .deal__price { color: var(--navy); font-weight: 700; }
  .deal--note { font-weight: 700; margin-top: 4px; }
</style>
</head>
<body>
  <main class="poster">
    <div class="poster__crowd" role="img" aria-label="Blurred nightclub crowd with bright stage lights and fans raising their arms"></div>

    <div class="brand">
      <span class="brand__name">THE<br>REBOUND</span>
      <span class="brand__area">HARBOR ROW</span>
    </div>

    <h1 class="headline headline--top">COMING</h1>
    <h1 class="headline headline--bottom">SOON!</h1>

    <p class="tagline">Be part of the first in line for the amazing things happening</p>

    <section class="deals">
      <h2 class="deals__title">PURCHASE THESE AMAZING DEALS FOR THE FIRST WEEKEND</h2>
      <div class="deals__columns">
        <div class="deals__col">
          <p class="deal"><span class="deal__price">$25</span> Opening Fri or Sat night Glitter Hour GA Ticket w/DQS Megastar: M (only 100 Available Per Night)</p>
          <p class="deal"><span class="deal__price">$50</span> Opening Fri or Sat Night Glitter Hour Third Tier Seating (Only 60 Available Per Night)</p>
          <p class="deal"><span class="deal__price">$75</span> Opening Fri or Sat Night Glitter Hour Middle Tier seating Ticket w/secret DQS Megastar. (Only 60 Available Per Night)</p>
          <p class="deal"><span class="deal__price">$100</span> Opening Fri or Sat Night Glitter Hour VIP Ticket w/secret DQS Megastar. (Only 60 Available Per Night)</p>
        </div>
        <div class="deals__col">
          <p class="deal"><span class="deal__price">$500</span> The Rebound Pass Skip the line and free cover for 6 months. Not including Brunch Shows and Special Events. Plus The Rebound Merch (50 Available)</p>
          <p class="deal"><span class="deal__price">$1000</span> The Rebound Gold Pass. Skip the line and free cover for the year. Not including Brunch Shows and Special Events Plus The Rebound Merch. (100 Available)</p>
          <p class="deal deal--note">*Ask about The Rebound Elite Pass</p>
        </div>
      </div>
    </section>
  </main>
</body>
</html>
```